Web Design Project + Development

We need a web design for a new company called Vireltan Group.
We are a young, financial company with a professional but playful culture.
I have attached the company logo.
I need design and development for this web site.
See below for site map
Landing Page
(Should have two tabs in the middle to lead into Vireltan Trading or Vireltan Capital)
Landing Page for Vireltan Trading
Welcome Page
Tabs on the top are (Home/About Us/FAQ/Careers/Contact Us)
Landing Page for Vireltan Capital
Welcome Page
Please submit design of landing pages ONLY.
Contents of the web site will be supplied after we select designer.
Look and feel of this website should be simple, crisp and professional but keeping to the brand logo, font and colours
Industry/Entity Type
Financial
Requirements
Must have
- please see below website of our desired look and feel.
http://www.qorbafunds.com.au/campaign/smsf/overview

```html
<!DOCTYPE html>
<html lang="en">
<head>
<meta charset="utf-8">
<title>Vireltan Group</title>
<link href="https://fonts.googleapis.com/css2?family=Source+Sans+3:wght@300;400;600&display=swap" rel="stylesheet">
<style>
:root{
  --header-bg:#ededee;
  --hero-top:#b6dbf5;
  --hero-bottom:#5ca2d8;
  --navy:#0d3b5f;
  --brand-blue:#1a5a94;
  --tab-text:#0e4b7e;
  --text:#3a3f47;
  --nav-text:#2f3338;
  --divider:#5ba3d9;
  --footer-bg:#373d45;
  --footer-text:#ffffff;
  --dot:#3d4a56;
  --dot-active:#0f4a80;
  --button-dark:#3a3f47;
  --white:#ffffff;
}
*{margin:0;padding:0;box-sizing:border-box}
html,body{width:1200px;height:874px;overflow:hidden}
body{font-family:"Source Sans 3",Arial,sans-serif;background:var(--header-bg);color:var(--text);position:relative}
.abs{position:absolute}

.site-header{position:absolute;left:0;top:0;width:1200px;height:85px;background:var(--header-bg)}
.brand{position:absolute;left:158px;top:22px;display:flex;align-items:center;gap:10px}
.brand-mark{width:30px;height:30px;border-radius:50%;background:var(--divider)}
.brand-name{font-size:26px;font-weight:600;color:#4a5058;letter-spacing:.3px}
.search{position:absolute;left:860px;top:12px;width:176px;height:27px;background:var(--white);border:1px solid #cfd2d5;font-size:11px;color:#555;padding:6px 7px}
.search svg{position:absolute;right:5px;top:5px}
.main-nav{position:absolute;right:164px;top:51px;display:flex;font-size:15.5px;color:var(--nav-text)}
.main-nav span{padding:0 12px;border-left:1px solid var(--divider);line-height:17px}
.main-nav span:first-child{border-left:none}
.main-nav span:last-child{padding-right:0}

.hero{position:absolute;left:0;top:85px;width:1200px;height:409px;background:linear-gradient(var(--hero-top),var(--hero-bottom))}
.hero-title{position:absolute;left:228px;top:56px;font-size:43px;font-weight:300;color:var(--white)}
.hero-lead{position:absolute;left:230px;top:114px;width:400px;font-size:20.5px;line-height:32px;color:#26323f}
.read-more{position:absolute;left:234px;top:200px;width:93px;height:34px;background:var(--navy);color:var(--white);font-size:13.5px;line-height:34px;text-align:center}
.dots{position:absolute;left:237px;top:312px;display:flex;gap:6px}
.dots i{width:12px;height:12px;border-radius:50%;background:var(--dot)}
.dots i.active{background:var(--dot-active)}
.arrow{position:absolute;width:24px;height:24px}
.video-card{position:absolute;left:677px;top:61px;width:302px;height:280px;background:var(--white)}
.video-still{position:absolute;left:2px;top:46px;width:298px;height:171px;background:linear-gradient(#f6f6f4,#eeeeec)}
.video-still svg{position:absolute;left:117px;top:53px}

.tab{position:absolute;top:454px;height:40px;background:var(--white);color:var(--tab-text);font-size:19px;line-height:44px;text-align:center}

.intro-title{position:absolute;left:167px;top:516px;font-size:19.5px;font-weight:300;color:var(--brand-blue)}
.coins{position:absolute;left:164px;top:553px;width:205px;height:200px;background:radial-gradient(circle at 45% 60%,#5b7d9a 0 22%,#c9a246 23% 55%,#ededee 75%)}
.intro-text{position:absolute;left:388px;top:563px;width:383px;font-size:13.3px;line-height:20.3px;text-align:justify;font-weight:300;color:#2f3338}
.intro-text p+p{margin-top:16px}

.about-title{position:absolute;left:807px;top:516px;font-size:19.5px;font-weight:300;color:var(--brand-blue)}
.about-photo{position:absolute;left:807px;top:548px;width:222px;height:76px;background:linear-gradient(90deg,#d9d5cd,#eef0f2 55%,#b7cde6)}
.about-text{position:absolute;left:808px;top:632px;width:220px;font-size:13.3px;line-height:20.3px;text-align:justify;font-weight:300;color:#2f3338}
.get-more{position:absolute;left:809px;top:722px;width:80px;height:24px;background:var(--button-dark);color:var(--white);font-size:13px;line-height:24px;text-align:center;font-weight:300}

.site-footer{position:absolute;left:0;top:789px;width:1200px;height:85px;background:var(--footer-bg);color:var(--footer-text);font-weight:300}
.follow{position:absolute;left:165px;top:15px;font-size:13.5px}
.social{position:absolute;left:166px;top:43px;display:flex;gap:7px}
.social i{width:22px;height:22px;border-radius:3px;background:#5a84b8}
.footer-nav{position:absolute;right:170px;top:15px;font-size:12.5px}
.footer-nav span{margin:0 4px}
.copyright{position:absolute;right:170px;top:36px;font-size:12.5px}
</style>
</head>
<body>

<header class="site-header">
  <div class="brand"><span class="brand-mark"></span><span class="brand-name">vireltan</span></div>
  <div class="search">Search
    <svg width="14" height="14" viewBox="0 0 14 14"><circle cx="5.5" cy="5.5" r="3.8" fill="none" stroke="#333" stroke-width="1.6"/><line x1="8.3" y1="8.3" x2="12.5" y2="12.5" stroke="#333" stroke-width="2"/></svg>
  </div>
  <nav class="main-nav"><span>Home</span><span>About Us</span><span>FAQ</span><span>Careers</span><span>Contact Us</span></nav>
</header>

<section class="hero">
  <h1 class="hero-title">Welcome to Our Site</h1>
  <p class="hero-lead">Lorem Ipsum is simply dummy text of the printing and typesetting industry.</p>
  <div class="read-more">READ MORE</div>
  <div class="dots"><i></i><i></i><i class="active"></i><i></i><i></i></div>

  <svg class="arrow" style="left:151px;top:181px" viewBox="0 0 24 24"><circle cx="12" cy="12" r="11" fill="#f4f4f4" stroke="#8a8f95"/><path d="M12 8 L8 12 L12 16Z M16 8 L12 12 L16 16Z" fill="#333"/></svg>
  <svg class="arrow" style="left:1012px;top:185px" viewBox="0 0 24 24"><circle cx="12" cy="12" r="11" fill="#f4f4f4" stroke="#8a8f95"/><path d="M8 8 L12 12 L8 16Z M12 8 L16 12 L12 16Z" fill="#333"/></svg>

  <div class="video-card">
    <div class="video-still" role="img" aria-label="Video still: infographic on investor needs such as capital growth, diversification, regular income and capital stability">
      <svg width="64" height="64" viewBox="0 0 64 64"><circle cx="32" cy="32" r="30" fill="#e6e8ea" fill-opacity=".85" stroke="#b9bec4" stroke-width="2"/><path d="M25 18 L47 32 L25 46Z" fill="#fff" stroke="#b9bec4" stroke-width="1.5"/></svg>
    </div>
  </div>
</section>

<div class="tab" style="left:165px;width:190px">Vireltan Trading</div>
<div class="tab" style="left:366px;width:189px">Vireltan Capital</div>

<h2 class="intro-title">Lorem Ipsum is simply dummy text of the</h2>
<div class="coins" role="img" aria-label="Photo of a globe among stacks of gold coins"></div>
<div class="intro-text">
  <p>Lorem Ipsum has been the industry's standard dummy text ever since the 1500s, when an unknown printer took a galley of type and scrambled it to make a type specimen book. It has survived not only five centuries, but also the leap into electronic typesetting, remaining essentially unchanged</p>
  <p>Contrary to popular belief, Lorem Ipsum is not simply random text. It has roots in a piece of classical Latin literature from 45 BC, making it over 2000 years old.</p>
</div>

<h2 class="about-title">About Us</h2>
<div class="about-photo" role="img" aria-label="Photo of an adviser meeting with a couple in a bright office"></div>
<p class="about-text">Lorem Ipsum has been the industry's standard dummy text ever since the 1500s, when an unknown printer took a galley.</p>
<div class="get-more">Get More</div>

<footer class="site-footer">
  <div class="follow">Follow Us On</div>
  <div class="social" role="img" aria-label="Social network links"><i></i><i></i><i></i><i></i></div>
  <div class="footer-nav">Home<span>/</span>About Us<span>/</span>FAQ<span>/</span>Careers<span>/</span>Contact Us</div>
  <div class="copyright">Copyrights @ 2013 All Rights Reserved</div>
</footer>

</body>
</html>
```